Our Company name is Bluefinch Office Cleaning Services. We are a Toronto(GTA) company looking for a brochure that with Logo design that gives a description of what we do.

We are a company that specializes in cleaning and sanitizing office/ workplaces. Our Experience includes working with school boards and hospitals, and have 15 plus years experience. We are looking for a simple design that catches and explains to our customers what we offer with some pics, which you can provide.

if you have any questions please let us know.

thank you

Target Market(s)

We are focusing Businesses

Font styles to use
Serif

Colors

Designer to choose colors to be used in the design.

Requirements
Must have
• Must have our name/Logo, brief description of what we do. Contact numbers, (416)-284-7316/ (647)591-2637 email (bluefinchofficecleaningservices@mailtrove.com
• Pics which you can provide
Nice to have
• We trust your imagination on this

```html
<!DOCTYPE html>
<html lang="en">
<head>
<meta charset="utf-8">
<title>Bluefinch Office Cleaning Services – Brochure Outside</title>
<link href="https://fonts.googleapis.com/css2?family=Kaushan+Script&family=Roboto:wght@300;400;500;700&display=swap" rel="stylesheet">
<style>
  :root{
    --navy:#231657;
    --navy-deep:#1a0f45;
    --violet:#4f3a9c;
    --yellow:#f2c81b;
    --ink:#222;
    --white:#fff;
    --page:#e9e9e9;
  }
  *{margin:0;padding:0;box-sizing:border-box}
  html,body{width:817px;height:1200px;overflow:hidden;background:var(--page);font-family:"Roboto",Arial,sans-serif}
  .brochure{position:absolute;left:3px;top:286px;width:810px;height:628px;background:var(--white);box-shadow:0 6px 22px rgba(0,0,0,.22);overflow:hidden}
  .shapes{position:absolute;inset:0}
  .panel{position:absolute;top:0;height:628px}
  .panel--left{left:0;width:263px}
  .panel--middle{left:263px;width:267px}
  .panel--right{left:530px;width:280px}
  .pill{position:absolute;left:54px;width:152px;height:26px;border-radius:13px;font-family:"Kaushan Script",cursive;font-size:15px;line-height:26px;text-align:center;box-shadow:0 2px 3px rgba(0,0,0,.25)}
  .pill--violet{background:var(--violet);color:var(--white)}
  .pill--yellow{background:var(--yellow);color:var(--navy)}
  .copy{position:absolute;left:16px;width:232px;font-size:9px;line-height:12px;color:var(--ink)}
  .copy--center{text-align:center}
  .copy p+p{margin-top:5px}
  .provide-list{position:absolute;left:10px;width:243px;list-style:none;text-align:center;font-size:9px;color:var(--ink)}
  .provide-list li{height:20px;line-height:20px;font-weight:500}
  .intro{position:absolute;top:20px;left:18px;width:231px;text-align:center;font-size:12px;line-height:15.5px;color:var(--ink)}
  .intro b{color:var(--yellow);font-weight:700}
  .script{font-family:"Kaushan Script",cursive;color:var(--yellow)}
  .service-title{position:absolute;top:278px;left:0;width:267px;text-align:center}
  .service-title .script{display:block;font-size:25px;line-height:30px}
  .service-title .caps{display:block;font-size:12.5px;color:var(--white);letter-spacing:.3px}
  .service-list{position:absolute;top:328px;left:0;width:267px;text-align:center;font-size:9px;line-height:12px;color:var(--white)}
  .brand-name{color:var(--violet);font-weight:700;text-align:center}
  .brand-name span{display:block}
  .brand-name--small{position:absolute;top:408px;left:0;width:267px;color:var(--yellow)}
  .brand-name--small .big{font-size:19px;line-height:20px}
  .brand-name--small .mid{font-size:9px;line-height:11px}
  .brand-name--small .tiny{font-size:5.5px;letter-spacing:4px;line-height:8px}
  .contact-title{position:absolute;top:474px;left:0;width:267px;text-align:center;font-family:"Kaushan Script",cursive;font-size:17px;color:var(--white)}
  .contact-icons{position:absolute;top:514px;left:98px}
  .phones{position:absolute;top:548px;left:0;width:267px;text-align:center;color:var(--yellow);font-weight:700;font-size:18px;line-height:21px}
  .email{position:absolute;top:596px;left:0;width:267px;text-align:center;color:var(--white);font-size:9.5px;letter-spacing:-.1px}
  .brand-name--large{position:absolute;top:18px;left:40px;width:220px}
  .brand-name--large .big{font-size:40px;line-height:44px}
  .brand-name--large .mid{font-size:21px;line-height:24px}
  .brand-name--large .tiny{font-size:10px;letter-spacing:11px;line-height:18px;padding-left:11px}
  .headline{position:absolute;top:430px;left:56px;width:220px;color:var(--white)}
  .headline .thin{display:block;font-weight:300;font-size:24px;letter-spacing:1px;line-height:28px}
  .headline .script{display:block;font-size:40px;line-height:46px}
  .headline .plain{display:block;font-size:21px;line-height:24px}
  .tagline{position:absolute;top:553px;left:22px;width:240px;text-align:center;color:var(--white);font-size:8px;line-height:11px}
</style>
</head>
<body>
<main class="brochure">
  <svg class="shapes" width="810" height="628" viewBox="0 0 810 628" xmlns="http://www.w3.org/2000/svg">
    <defs>
      <linearGradient id="leftBg" x1="0" y1="0" x2="1" y2="0">
        <stop offset="0" stop-color="#f1f1f1"/><stop offset="1" stop-color="#ffffff"/>
      </linearGradient>
      <linearGradient id="roomTone" x1="0" y1="0" x2="0" y2="1">
        <stop offset="0" stop-color="#d9d7d3"/><stop offset="1" stop-color="#8d8c8c"/>
      </linearGradient>
      <linearGradient id="officeTone" x1="0" y1="0" x2="1" y2="1">
        <stop offset="0" stop-color="#e6e8ec"/><stop offset=".6" stop-color="#aeb6c4"/><stop offset="1" stop-color="#3f5fa8"/>
      </linearGradient>
      <radialGradient id="bathTone"><stop offset="0" stop-color="#f2eee9"/><stop offset="1" stop-color="#b9b2a8"/></radialGradient>
      <radialGradient id="meetingTone"><stop offset="0" stop-color="#f6f6f6"/><stop offset="1" stop-color="#b8b4ae"/></radialGradient>
      <radialGradient id="navyGlow" cx=".5" cy=".6" r=".7"><stop offset="0" stop-color="#2c1d6a"/><stop offset="1" stop-color="#1a0f45"/></radialGradient>
    </defs>

    <!-- left panel -->
    <rect x="0" y="0" width="263" height="628" fill="url(#leftBg)"/>
    <g role="img" aria-label="Photo of a clean living room with a grey sofa and chair">
      <path d="M0 468 C90 482 200 455 263 392 L263 606 L0 606 Z" fill="url(#roomTone)"/>
    </g>
    <path d="M0 462 C90 476 200 448 263 386 L263 392 C200 455 90 482 0 468 Z" fill="var(--violet)"/>
    <path d="M0 478 C100 492 215 462 263 395 L263 402 C210 470 100 498 0 486 Z" fill="var(--yellow)"/>

    <!-- middle panel -->
    <rect x="263" y="0" width="267" height="628" fill="var(--white)"/>
    <path d="M263 168 C330 160 430 130 530 85 L530 230 L263 230 Z" fill="var(--yellow)"/>
    <path d="M263 214 C335 205 430 170 530 112 L530 606 L263 606 Z" fill="url(#navyGlow)"/>

    <!-- right panel -->
    <rect x="530" y="0" width="280" height="628" fill="var(--white)"/>
    <path d="M530 112 C640 150 730 150 810 120 L810 606 L530 606 Z" fill="var(--yellow)"/>
    <path d="M530 124 C640 160 730 160 810 132 L810 606 L530 606 Z" fill="url(#navyGlow)"/>
    <g role="img" aria-label="Photo of a cleaning team in blue uniforms cleaning an office">
      <path d="M530 140 C640 170 730 168 810 142 L810 400 C740 415 640 380 560 392 C545 395 535 400 530 404 Z" fill="url(#officeTone)"/>
    </g>
    <path d="M530 404 C560 380 640 380 740 402 C770 408 795 404 810 398 L810 410 C780 422 740 420 690 412 C620 400 560 400 530 418 Z" fill="var(--yellow)"/>
    <path d="M530 418 C560 402 620 402 690 414 C740 422 780 424 810 412 L810 418 C780 430 740 428 690 420 C620 410 560 410 530 426 Z" fill="var(--violet)"/>

    <!-- circular photos -->
    <g role="img" aria-label="Round photo of a clean white bathroom">
      <circle cx="125" cy="468" r="60" fill="#fff"/>
      <circle cx="125" cy="468" r="55" fill="url(#bathTone)"/>
    </g>
    <g role="img" aria-label="Round photo of a bright empty meeting room with a table and chairs">
      <circle cx="397" cy="193" r="75" fill="#fff"/>
      <circle cx="397" cy="193" r="70" fill="url(#meetingTone)"/>
    </g>

    <!-- panel folds and bottom band -->
    <rect x="0" y="606" width="810" height="22" fill="var(--yellow)"/>
    <line x1="263" y1="0" x2="263" y2="628" stroke="rgba(0,0,0,.08)"/>
    <line x1="530" y1="0" x2="530" y2="628" stroke="rgba(0,0,0,.08)"/>
  </svg>

  <section class="panel panel--left">
    <div class="pill pill--violet" style="top:22px">Facilities Management</div>
    <div class="copy copy--center" style="top:60px">We deliver a wide range of facilities management services specifically tailored to suit our client's requirements.</div>
    <div class="pill pill--yellow" style="top:114px">Service Solution</div>
    <div class="copy" style="top:154px">
      <p>We utilise unique time and attendance software to monitor staff attendance to properties.</p>
      <p>Our electronic auditing solution gives measurable service performance, trend analysis and reporting.</p>
    </div>
    <div class="pill pill--violet" style="top:234px">We Provide</div>
    <ul class="provide-list" style="top:276px">
      <li>Reliable, competent and motivated staff.</li>
      <li>Proactive communication.</li>
      <li>Highly visible management presence.</li>
      <li>A flexible approach to meet changing needs.</li>
      <li>Regular monitoring of contracts.</li>
      <li>Ongoing Health &amp; Safety reviews.</li>
    </ul>
  </section>

  <section class="panel panel--middle">
    <p class="intro">We adopt a highly <b>flexible approach</b> to the provision of consistently high quality and reliable cleaning to meet the demands of an ever changing <b>work environment.</b></p>
    <h2 class="service-title"><span class="script">Commercial</span><span class="caps">OFFICE CLEANING</span></h2>
    <p class="service-list">Reception and Communal Areas,<br>Executive Suites,<br>Open Plan and Private Work Areas,<br>Meeting Rooms,<br>Staff Rooms, Toilets &amp; Wash Rooms</p>
    <div class="brand-name brand-name--small"><span class="big">Bluefinch</span><span class="mid">Office Cleaning</span><span class="tiny">SERVICES</span></div>
    <h3 class="contact-title">Contact Us</h3>
    <svg class="contact-icons" width="72" height="26" viewBox="0 0 72 26" xmlns="http://www.w3.org/2000/svg">
      <rect x="4" y="4" width="18" height="18" transform="rotate(45 13 13)" fill="none" stroke="#fff" stroke-width="1.2"/>
      <path d="M9.5 8.5 C9 12 12 16.5 16.5 17.5 L17.5 15.5 L15.5 14 L14 15 C12.5 14 11.5 13 11 11.5 L12 10 L10.5 8 Z" fill="#fff"/>
      <rect x="50" y="4" width="18" height="18" transform="rotate(45 59 13)" fill="none" stroke="#fff" stroke-width="1.2"/>
      <rect x="53.5" y="9.5" width="11" height="7.5" fill="#fff"/>
      <path d="M53.5 9.5 L59 14 L64.5 9.5" fill="none" stroke="var(--navy)" stroke-width="1"/>
    </svg>
    <p class="phones">(416)-284-7316<br>(647)591-2637</p>
    <p class="email">bluefinchofficecleaningservices@mailtrove.com</p>
  </section>

  <section class="panel panel--right">
    <div class="brand-name brand-name--large"><span class="big">Bluefinch</span><span class="mid">Office Cleaning</span><span class="tiny">SERVICES</span></div>
    <h1 class="headline"><span class="thin">Creating</span><span class="script">Excellent</span><span class="plain">First Impressions</span></h1>
    <p class="tagline">We recognise that the presentation and standard of cleanliness of your premises have a significant impact on the perception of your business.</p>
  </section>
</main>
</body>
</html>
```